Business Card Design for new logo

Business card Design for new logo. Follow colors from logo.
The company has offices in multiple comtries
Want to have some bulltes on the countries and also on the main services

Something like
USA*Dominican Republic*LATAM

Consulting*Healthcare IT*Tranformation

Industry/Entity Type

Information Technology

Contact Information for Business Card

Address, Phones, countries, name and position

Miron castell

Founder and CEO

947 Quarry Ln
Mill haven, PA 16835

Mcastell@novelquin.com

www.novelquin.com

717-352-6081

828-444-4444

```html
<!DOCTYPE html>
<html lang="en">
<head>
<meta charset="utf-8">
<title>Novelquin Business Card</title>
<link href="https://fonts.googleapis.com/css2?family=Open+Sans:wght@400;600;700&display=swap" rel="stylesheet">
<style>
  :root {
    --backdrop: #e9e4dc;
    --kraft-light: #d2ab7b;
    --kraft-mid: #c59a68;
    --kraft-dark: #b4865a;
    --ink: #17110a;
    --rule: #5c4630;
  }
  * { margin: 0; padding: 0; box-sizing: border-box; }
  html, body {
    width: 1200px;
    height: 900px;
    overflow: hidden;
    background: var(--backdrop);
    font-family: "Open Sans", Arial, sans-serif;
    color: var(--ink);
  }
  .stage { position: relative; width: 1200px; height: 900px; }
  .card {
    position: absolute;
    left: 330px;
    width: 556px;
    height: 343px;
    background: radial-gradient(ellipse at 35% 20%, var(--kraft-light) 0%, var(--kraft-mid) 55%, var(--kraft-dark) 100%);
  }
  .card--front { top: 90px; }
  .card--back { top: 470px; }

  .contact {
    position: absolute;
    left: 0; right: 0; top: 74px;
    text-align: center;
    font-size: 16px;
    line-height: 20px;
  }
  .contact__name { font-size: 23px; font-weight: 600; line-height: 28px; }
  .contact__rule {
    width: 137px;
    height: 1px;
    background: var(--rule);
    margin: 6px auto 6px;
  }
  .contact__label { font-weight: 700; }
  .contact__web { font-weight: 700; }

  .brand {
    position: absolute;
    left: 0; right: 0; top: 150px;
    display: flex;
    align-items: center;
    justify-content: center;
    gap: 16px;
  }
  .brand__dot {
    width: 30px; height: 30px;
    border-radius: 50%;
    background: var(--ink);
  }
  .brand__name {
    font-size: 44px;
    font-weight: 600;
    line-height: 56px;
    color: var(--ink);
  }
  .back__rule {
    position: absolute;
    left: 50px; width: 459px; top: 235px;
    height: 1px;
    background: var(--rule);
  }
  .bullets {
    position: absolute;
    top: 251px;
    list-style: none;
    font-size: 16px;
    line-height: 20px;
  }
  .bullets--services { left: 45px; }
  .bullets--regions { left: 345px; }
  .bullets li::before {
    content: "";
    display: inline-block;
    width: 10px; height: 10px;
    border-radius: 50%;
    background: var(--ink);
    margin-right: 3px;
    vertical-align: 0;
  }
</style>
</head>
<body>
<main class="stage">
  <section class="card card--front">
    <div class="contact">
      <p class="contact__name">Miron castell</p>
      <p class="contact__title">Founder and CEO</p>
      <div class="contact__rule"></div>
      <p>947 Quarry Ln</p>
      <p>Mill haven, PA 16835</p>
      <div class="contact__rule"></div>
      <p><span class="contact__label">P:</span> 717-352-6081</p>
      <p><span class="contact__label">M:</span> 828-444-4444</p>
      <p><span class="contact__label">E:</span> Mcastell@novelquin.com</p>
      <p class="contact__web">www.novelquin.com</p>
    </div>
  </section>

  <section class="card card--back">
    <div class="brand">
      <span class="brand__dot"></span>
      <span class="brand__name">Novelquin</span>
    </div>
    <div class="back__rule"></div>
    <ul class="bullets bullets--services">
      <li>Consulting</li>
      <li>Healthcare IT</li>
      <li>Tranformation</li>
    </ul>
    <ul class="bullets bullets--regions">
      <li>USA</li>
      <li>Dominican Republic</li>
      <li>LATAM</li>
    </ul>
  </section>
</main>
</body>
</html>
```